Photojournalism/photography business needs a simple, timeless & professional letterhead design

We need a letterhead design for photography/photojournalism business called 'plomk', no capitals.

The letterhead needs to be:
- simple
- professional
- timeless
- easy to read
- consists of at least 2 colors to make it stands out.

We do mainly editorial photography, photo articles for various publications, travel, businesses, as well as people such as family and kids.

The final design should communicate professionalism, easy identification, attention grabbing, even if it has to be found among a stack of various papers on the clients' desks.

Target Market(s)

Various publications.

Industry/Entity Type

Business

Requirements
Must have
• Please use the logo attached.

```html
<!DOCTYPE html>
<html lang="en">
<head>
<meta charset="utf-8">
<title>plomk stationery</title>
<link rel="stylesheet" href="https://fonts.googleapis.com/css2?family=PT+Serif:wght@400;700&display=swap">
<style>
  :root {
    --bg: #000000;
    --green: #6b9a73;
    --green-light: #b4c8b2;
    --green-dark: #1d5b3d;
    --paper: #ffffff;
    --paper-shade: #f1f1f1;
    --ink: #2a2a2a;
    --rule: #444444;
  }
  html, body {
    margin: 0;
    padding: 0;
    width: 1200px;
    height: 848px;
    overflow: hidden;
    background: var(--bg);
    font-family: "PT Serif", Georgia, serif;
  }
  .canvas { position: relative; width: 1200px; height: 848px; }

  .brand-name {
    font-family: "PT Serif", Georgia, serif;
    font-weight: 700;
    color: var(--green-dark);
    letter-spacing: -0.02em;
    line-height: 1;
    position: absolute;
  }

  /* Folder */
  .folder {
    position: absolute; left: 118px; top: 137px;
    width: 442px; height: 624px;
    background: var(--green);
  }
  .folder .brand-name { left: 150px; top: 283px; font-size: 52px; }

  /* Letterhead */
  .letterhead {
    position: absolute; left: 422px; top: 66px;
    width: 441px; height: 623px;
    background: linear-gradient(180deg, var(--paper) 0%, var(--paper-shade) 100%);
  }
  .letterhead .brand-name { left: 22px; top: 24px; font-size: 36px; }
  .letterhead .header-rule {
    position: absolute; left: 125px; top: 67px;
    width: 250px; height: 1px; background: var(--rule);
  }
  .letterhead .sender {
    position: absolute; left: 30px; top: 90px;
    width: 100px; margin: 0;
    font-size: 5.5px; line-height: 7.3px; color: var(--ink);
  }
  .letterhead .body-copy {
    position: absolute; left: 120px; top: 154px; width: 265px;
  }
  .letterhead .body-copy p {
    margin: 0 0 13.4px;
    font-size: 7.2px; line-height: 13.4px;
    letter-spacing: 0.06em; text-align: justify; color: var(--ink);
  }
  .letterhead .footer-band {
    position: absolute; left: 0; bottom: 0;
    width: 100%; height: 43px;
    background: var(--green);
    border-top: 4px solid var(--green-light);
  }

  /* Envelope back */
  .envelope-back {
    position: absolute; left: 621px; top: 162px;
    width: 489px; height: 218px;
    background: var(--paper);
  }
  .envelope-back svg { position: absolute; left: 0; top: 0; }

  /* Envelope front */
  .envelope-front {
    position: absolute; left: 618px; top: 412px;
    width: 490px; height: 218px;
    background: var(--paper);
  }
  .envelope-front .brand-name { left: 46px; top: 8px; font-size: 34px; }
  .envelope-front .return-band {
    position: absolute; left: 0; bottom: 0;
    width: 100%; height: 42px;
    background: var(--green);
    border-top: 3px solid var(--green-light);
  }
  .envelope-front .return-address {
    position: absolute; left: 36px; top: 4px;
    width: 118px; margin: 0;
    font-size: 5.6px; line-height: 8.4px;
    text-align: center; color: var(--paper);
  }
</style>
</head>
<body>
<main class="canvas">

  <section class="folder" aria-label="Presentation folder">
    <span class="brand-name">plomk</span>
  </section>

  <section class="letterhead" aria-label="Letterhead">
    <span class="brand-name">plomk</span>
    <div class="header-rule"></div>
    <p class="sender">Lorem ipsum dolor sit amet, consectetur adipisicing elit, sed do eiusmod tempor incididunt ut labore et dolore<br>www.plomk.com.au<br>0412 555 019</p>
    <div class="body-copy">
      <p>Lorem ipsum dolor sit amet, consectetur adipisicing elit, sed do eiusmod tempor incididunt ut labore et dolore magna aliqua. Ut enim ad minim veniam, quis nostrud exercitation ullamco laboris nisi ut aliquip ex ea commodo consequat. Duis aute irure dolor in reprehenderit in voluptate velit esse cillum dolore eu fugiat nulla pariatur. Excepteur sint occaecat cupidatat non proident, sunt in culpa qui officia deserunt mollit anim id est laborum.</p>
      <p>Lorem ipsum dolor sit amet, consectetur adipisicing elit, sed do eiusmod tempor incididunt ut labore et dolore magna aliqua. Ut enim ad minim veniam, quis nostrud exercitation ullamco laboris nisi ut aliquip ex ea commodo consequat. Duis aute irure dolor in reprehenderit in voluptate velit esse cillum dolore eu fugiat nulla pariatur. Excepteur sint occaecat cupidatat non proident, sunt in culpa qui officia deserunt mollit anim id est laborum.</p>
      <p>Lorem ipsum dolor sit amet, consectetur adipisicing elit, sed do eiusmod tempor incididunt ut labore et dolore magna aliqua. Ut enim ad minim veniam, quis nostrud exercitation ullamco laboris nisi ut aliquip ex ea commodo consequat. Duis aute irure dolor in reprehenderit in voluptate velit esse cillum dolore eu fugiat nulla pariatur. Excepteur sint occaecat cupidatat non proident, sunt in culpa qui officia deserunt mollit anim id est laborum.</p>
      <p>Lorem ipsum dolor sit amet, consectetur adipisicing elit, sed do eiusmod tempor incididunt ut labore et dolore magna aliqua. Ut enim ad minim veniam, quis nostrud exercitation ullamco laboris nisi ut aliquip ex ea commodo consequat.</p>
    </div>
    <div class="footer-band"></div>
  </section>

  <section class="envelope-back" aria-label="Envelope back">
    <svg width="489" height="218" viewBox="0 0 489 218" aria-hidden="true">
      <polygon points="0,0 489,0 484,68 6,68" fill="var(--green)"/>
    </svg>
  </section>

  <section class="envelope-front" aria-label="Envelope front">
    <span class="brand-name">plomk</span>
    <div class="return-band">
      <p class="return-address">Lorem ipsum dolor sit amet, consectetur adipisicing elit, sed do<br>www.plomk.com.au<br>0412 555 019</p>
    </div>
  </section>

</main>
</body>
</html>
```